Book Cover for Memoir: Sexual Assault and Traumatic Stress

I need a cover design for a memoir that is a victim's story of a sexual assault. I will need a print-on-demand cover, an eBook cover, and a 3D thumbnail image. The thumbnail and eBook cover will be used immediately, and the POD cover will be used in a few months with the full manuscript is ready. Therefore, I need an artist who is willing to make small adjustments if needed once the page count is set.

I have a image I have purchased that should give you an idea of the desired direction, but you can feel free to use your own images. I have attached some examples of book covers I like. I attached a color palette for fonts.

Overall Look: Fonts should be feminine and thin, but large to stand out. Look should be simple and elegant, and display and overall depressing feeling. There should be enough detail though to make it look professionally put together. Not TOO minimalistic.

I have also attached the Print Harbor templates if you choose to use those. If not, ensure there is an open place for the barcode on the bottom right.

Requirements
Must have
• Title: Beneath Quiet Rain
Subtitle: One Woman's Account of Fear, Guilt & Silence
Author: Dana Ruth Whitford
Audience: Mostly women 18-30
Quote (for the back): "I always thought I'd know how I'd react if I ever was raped. I was wrong. I've been wrong a lot lately."
Summary (back cover): When twenty-seven-year-old Dana Whitford wakes up with a gut-wrenching feeling, she has little memory of the horrifying events that occurred the night before. Days earlier, Dana was a spirited single mom who had abandoned her hometown to raise her daughter in the city and pursue her dreams. In the short months since Dana’s move to Seattle, she became the adored lover of a charismatic lawyer, started a new business, and finally felt life was going her way. So what happened to cause her to break?

In a gripping and heartbreaking narrative, Dana tells the true story of how her life unraveled from the traumatic events that took place that night and why what seems obvious to everyone else is impossible for Dana to believe. Beneath Quiet Rain is a chilling exploration of memory through trauma, trust in humanity, and a captivating story of strength and survival that appeals to the heart of fathers and mothers, sons and daughters, and men and women alike.
Nice to have
• BACK COVER: I'd like to have a photo on the back. This should depict the happy life of the main character before the sexual assault, and should be with her daughter. Or should be a nature scene that starts at the corner and blends into the rest of the cover. I have attached a possible image or you can use something you like.

```html
<!DOCTYPE html>
<html lang="en">
<head>
<meta charset="utf-8">
<title>Beneath Quiet Rain — Dana Ruth Whitford</title>
<link rel="stylesheet" href="https://fonts.googleapis.com/css2?family=Raleway:wght@200;300;400&display=swap">
<style>
  :root {
    --stage: #e9e9ea;
    --cover-pale: #f3ece9;
    --cover-blush: #ead8d6;
    --water-grey: #a9b2b1;
    --hair-navy: #2e3350;
    --skin: #f1dcd4;
    --title-red: #df4a5c;
    --title-red-deep: #c2344a;
    --author-white: #f7f5f4;
    --subtitle-ink: #3b3a44;
  }
  * { margin: 0; padding: 0; box-sizing: border-box; }
  html, body {
    width: 1200px;
    height: 900px;
    overflow: hidden;
    background: var(--stage);
  }
  .stage {
    position: relative;
    width: 1200px;
    height: 900px;
    display: flex;
    align-items: center;
    justify-content: center;
  }
  .cover {
    position: relative;
    width: 600px;
    height: 900px;
    overflow: hidden;
    background: var(--cover-pale);
    font-family: "Raleway", "Helvetica Neue", Arial, sans-serif;
  }
  .cover-photo {
    position: absolute;
    inset: 0;
    background:
      radial-gradient(ellipse 55% 40% at 78% 12%, var(--hair-navy) 0%, rgba(46,51,80,0.55) 45%, rgba(46,51,80,0) 75%),
      radial-gradient(ellipse 40% 30% at 38% 26%, var(--skin) 0%, rgba(241,220,212,0) 80%),
      radial-gradient(ellipse 50% 35% at 85% 45%, var(--water-grey) 0%, rgba(169,178,177,0) 80%),
      linear-gradient(180deg, #c9cccf 0%, var(--cover-blush) 40%, var(--cover-pale) 70%, #f6f1ef 100%);
  }
  .author {
    position: absolute;
    top: 10px;
    left: 0;
    right: 0;
    text-align: center;
    font-weight: 300;
    font-size: 38px;
    letter-spacing: 0.5px;
    color: var(--author-white);
    text-shadow: 0 1px 3px rgba(0,0,0,0.25);
  }
  .title {
    position: absolute;
    right: 98px;
    top: 500px;
    width: 400px;
    text-align: right;
    font-weight: 200;
    color: var(--title-red);
    text-transform: uppercase;
    line-height: 1;
    text-shadow: 0 1px 0 var(--title-red-deep), 0 2px 3px rgba(120,20,40,0.25);
  }
  .title-line { display: block; }
  .title-line--first { font-size: 82px; letter-spacing: 2px; }
  .title-line--second { font-size: 114px; letter-spacing: 4px; margin-top: 10px; }
  .title-line--third { font-size: 146px; letter-spacing: 8px; margin-top: 2px; }
  .subtitle {
    position: absolute;
    left: 0;
    right: 0;
    bottom: 20px;
    padding-left: 100px;
    font-weight: 400;
    font-size: 15.5px;
    color: var(--subtitle-ink);
  }
</style>
</head>
<body>
  <main class="stage">
    <section class="cover">
      <div class="cover-photo" role="img" aria-label="Photograph of a young woman with dark hair lying in pale water, wearing a pearl necklace and bracelet"></div>
      <p class="author">Dana Ruth Whitford</p>
      <h1 class="title">
        <span class="title-line title-line--first">Beneath</span>
        <span class="title-line title-line--second">Quiet</span>
        <span class="title-line title-line--third">Rain</span>
      </h1>
      <p class="subtitle">One Woman's Account of Fear, Guilt &amp; Silence</p>
    </section>
  </main>
</body>
</html>
```